Hi everyone,
Bright Nest Homes is a business that renovates older houses into modern homes. I'm looking for a design that is clean and simple. It needs to show the client that renovating is a simple process. No more than 3 colours to be used thanks.

What I need:
1. Logo
2. Business card (one side)
3. Letter head (A4)

Looking forward to the designs!

Industry/Entity Type

Construction

Logo Text

Bright Nest Homes

Font styles to use
Sans Serif

Requirements
Must have
• Trading name: Bright Nest Homes
• Contact name: Declan Ferris
• Email: declanferris@brightnesthomes.com.au
• Tel: 0417 582 046
• Clean and simple
Nice to have
• If design might include a few tools. eg Hammer, paint roller etc.
Should not have
• Complicated design

```html
<!DOCTYPE html>
<html lang="en">
<head>
<meta charset="utf-8">
<title>Bright Nest Homes – Business Card</title>
<link rel="stylesheet" href="https://fonts.googleapis.com/css2?family=Arimo:wght@400;700&display=swap">
<style>
  :root {
    --brand-orange: #c84a2c;
    --brand-grey: #555858;
    --ink: #111111;
    --divider: #6b6b6b;
    --paper: #ffffff;
  }
  html, body {
    margin: 0;
    padding: 0;
    overflow: hidden;
    background: var(--paper);
  }
  .card {
    position: relative;
    width: 1200px;
    height: 686px;
    background: var(--paper);
    overflow: hidden;
    font-family: "Arimo", Arial, sans-serif;
  }
  .brand {
    position: absolute;
    left: 40px;
    top: 468px;
    display: flex;
    align-items: center;
    gap: 18px;
  }
  .brand-mark {
    width: 40px;
    height: 40px;
    background: var(--brand-orange);
  }
  .brand-name {
    font-weight: 700;
    font-size: 52px;
    line-height: 1;
    color: var(--brand-grey);
    letter-spacing: -0.5px;
    white-space: nowrap;
  }
  .divider {
    position: absolute;
    left: 659px;
    top: 37px;
    width: 2px;
    height: 611px;
    background: var(--divider);
  }
  .contact {
    position: absolute;
    left: 705px;
    top: 442px;
    color: var(--ink);
  }
  .contact-name {
    margin: 0 0 22px;
    font-weight: 700;
    font-size: 50px;
    line-height: 1;
    letter-spacing: 0.3px;
  }
  .contact-line {
    margin: 0 0 20px;
    font-weight: 400;
    font-size: 21px;
    line-height: 1.1;
  }
</style>
</head>
<body>
  <div class="card">
    <div class="brand">
      <span class="brand-mark"></span>
      <span class="brand-name">Bright Nest Homes</span>
    </div>

    <div class="divider" aria-hidden="true"></div>

    <div class="contact">
      <h1 class="contact-name">Declan Ferris</h1>
      <p class="contact-line">declanferris@brightnesthomes.com.au</p>
      <p class="contact-line">Tel: 0417 582 046</p>
    </div>
  </div>
</body>
</html>
```